Products & Services Postcard For our Vacuum Repair Store & Carpet Cleaning Company

SEE ATTACHED DOCUMENTS FOR FRONT AND BACK OF CARD.
Also, Brand logos are available in my attachments

We are a Retail Vacuum Repair shop and we also have Three carpet cleaning trucks that operate out of our location. In addition to servicing Vacuum Cleaners we also offer in home cleaning services that include: Carpet cleaning, upholstery cleaning, tile & Grout Cleaning, general cleaning services, move out clean ups, one time cleanings, post construction cleanup and strip & wax floorsWe Need to design a KTRW(nbfl kestrel lane route) postcard that shows and tells everything we do. Postcard should include all our services, have before and after pictures, list benefits of doing business with us and should have coupons attached to create urgency to call usWe:Fully Insured, commercial & Residential, free estimatesWe are the only Vacuum Store in area that is a Certified OTWAB Cleaner.Also, the only OTWAB Certified cleaner that services Vacuum Cleaners.We have a great reputation as a 5 Star Vacuum Service Station and Also a 5 Star Cleaning Company. We are a one stop shop for ALL your cleaning needs.Our goal is to educate customers and provide options.Goal of the card is to get customers to call or stop in for advice on both their vacuum cleaner and cleaning their homes. Goal is to get phone to ring or get people through the door.

Target Market(s)

Homeowners, People interested in clean

Colors

Designer to choose colors to be used in the design.

Requirements
Must have
• Before & After pics
• Coupons
• List of services
• Call to Action
• Address
• Phone #
Nice to have
• One side of postcard could be about our Vacuum Cleaner repair shop.
• The other side could be about our cleaning business

```html
<!DOCTYPE html>
<html lang="en">
<head>
<meta charset="UTF-8">
<title>Carpet Cleaning Postcard</title>
<link rel="stylesheet" href="https://fonts.googleapis.com/css2?family=Bebas+Neue&family=Lato:wght@400&family=Roboto:wght@400;500;700&display=swap">
<style>
  :root {
    --navy: #0b2d6e;
    --navy-dark: #061c47;
    --green: #7dc242;
    --red: #a8151f;
    --red-dark: #7d0f17;
    --white: #ffffff;
    --ink: #2b2b2b;
    --page: #e0e0e0;
  }
  * { box-sizing: border-box; margin: 0; padding: 0; }
  html, body { width: 1200px; height: 1200px; overflow: hidden; background: var(--page); }
  .postcard {
    position: absolute; left: 40px; top: 194px;
    width: 1120px; height: 811px; background: var(--white); overflow: hidden;
  }
  .postcard-art { position: absolute; inset: 0; width: 100%; height: 100%; }
  .logo {
    position: absolute; left: 686px; top: 30px; width: 182px;
    font-family: 'Roboto', sans-serif; font-weight: 700;
    font-size: 68px; line-height: 68px; text-align: center; letter-spacing: -0.5px;
  }
  .logo-top { display: block; color: var(--green); }
  .logo-bottom { display: block; color: var(--navy); }
  .headline {
    position: absolute; left: 423px; top: 175px; width: 697px; height: 88px;
    display: flex; align-items: center; justify-content: center;
    font-family: 'Bebas Neue', sans-serif; font-size: 56px; color: var(--white);
    padding: 4px 0 0 12px;
  }
  .services {
    position: absolute; left: 509px; top: 280px; width: 568px;
    font-family: 'Lato', sans-serif; color: var(--ink);
  }
  .services h2 {
    font-family: 'Roboto', sans-serif; font-weight: 500; color: var(--navy);
    font-size: 31px; line-height: 36px; margin-bottom: 6px;
  }
  .services p {
    font-size: 18.6px; line-height: 23.4px; text-align: justify; margin-bottom: 10px;
  }
  .contact {
    position: absolute; left: 36px; top: 660px;
    font-family: 'Roboto', sans-serif; color: var(--white);
  }
  .contact-row { display: flex; align-items: center; gap: 12px; }
  .contact-name { font-size: 40px; font-weight: 500; line-height: 50px; }
  .contact-detail { font-size: 21px; line-height: 35px; }
  .contact-row svg { flex: none; }
  .about {
    position: absolute; left: 415px; top: 724px; width: 665px;
    font-family: 'Roboto', sans-serif; font-size: 19px; line-height: 23.4px; color: var(--white);
  }
</style>
</head>
<body>
<div class="postcard">
  <svg class="postcard-art" viewBox="0 0 766 555" preserveAspectRatio="none">
    <defs>
      <linearGradient id="photoTone" x1="0" y1="0" x2="0" y2="1">
        <stop offset="0" stop-color="#e9ecef"/>
        <stop offset="0.55" stop-color="#d9cfc2"/>
        <stop offset="1" stop-color="#bdb8b2"/>
      </linearGradient>
    </defs>
    <path role="img" aria-label="Photo of a man vacuuming a carpet in a living room"
          d="M0 0 H185 C262 28 318 110 320 205 C322 280 300 330 282 360 L282 432 C200 424 90 428 0 448 Z"
          fill="url(#photoTone)"/>
    <path d="M185 0 C262 28 320 110 322 205 C324 280 305 325 285 350" fill="none" stroke="var(--green)" stroke-width="7"/>
    <path d="M289 120 L300 108 L300 120 Z" fill="var(--navy-dark)"/>
    <rect x="289" y="120" width="477" height="60" fill="var(--navy)"/>
    <path d="M300 432 C420 470 520 490 600 470 C680 450 740 410 766 385 L766 413 C720 442 660 478 565 481 C465 484 385 456 330 438 Z" fill="var(--green)"/>
    <path d="M0 448 C120 420 240 420 330 438 C420 460 500 484 580 481 C680 474 740 432 766 415 V555 H0 Z" fill="var(--navy)"/>
    <g class="save-badge" transform="rotate(-18 265 393)">
      <circle cx="265" cy="393" r="58" fill="var(--red)"/>
      <circle cx="265" cy="393" r="53" fill="var(--white)"/>
      <circle cx="265" cy="393" r="48" fill="none" stroke="var(--red)" stroke-width="2.5"/>
      <circle cx="265" cy="393" r="33" fill="none" stroke="var(--red)" stroke-width="2"/>
      <text x="265" y="362" text-anchor="middle" font-family="Roboto, sans-serif" font-weight="700" font-size="13" fill="var(--red)">SAVE</text>
      <text x="265" y="434" text-anchor="middle" font-family="Roboto, sans-serif" font-weight="700" font-size="13" fill="var(--red)">SAVE</text>
      <text x="265" y="377" text-anchor="middle" font-size="9" fill="var(--red)">★ ★ ★</text>
      <text x="265" y="418" text-anchor="middle" font-size="9" fill="var(--red)">★ ★ ★</text>
      <path d="M190 382 L205 382 L200 392 L205 402 L190 402 Z" fill="var(--red-dark)"/>
      <path d="M345 382 L330 382 L335 392 L330 402 L345 402 Z" fill="var(--red-dark)"/>
      <rect x="203" y="380" width="130" height="24" fill="var(--red)"/>
      <text x="268" y="399" text-anchor="middle" font-family="Roboto, sans-serif" font-weight="700" font-size="18" fill="var(--white)">10% off</text>
    </g>
  </svg>

  <div class="logo"><span class="logo-top">OUR</span><span class="logo-bottom">LOGO</span></div>
  <div class="headline">You Will Love Your Carpet Again</div>

  <section class="services">
    <h2>What We Do</h2>
    <p>Fully Insured, commercial &amp; Residential, free estimates</p>
    <p>We are the only Vacuum Store in area that is a Certified OTWAB Cleaner. Also, the only OTWAB Certified cleaner that services Vacuum Cleaners.</p>
    <p>We have a great reputation as a 5 Star Vacuum Service Station and Also a 5 Star Cleaning Company. We are a one stop shop for ALL your cleaning needs. Our goal is to educate customers and provide options.</p>
    <p>Goal of the card is to get customers to call or stop in for advice on both their vacuum cleaner and cleaning their homes. Goal is to get phone to ring or get people through the door.</p>
  </section>

  <div class="contact">
    <div class="contact-row contact-name">
      <svg width="26" height="26" viewBox="0 0 24 24"><circle cx="12" cy="12" r="12" fill="var(--white)"/><path d="M8 6.5 L10 6 L11 9 L9.8 10 C10.5 11.8 12 13.3 13.8 14 L14.8 12.8 L17.8 13.8 L17.3 15.8 C15.5 18 7.5 12 8 6.5 Z" fill="var(--navy)"/></svg>
      <span>Lorem Ipsum</span>
    </div>
    <div class="contact-row contact-detail">
      <svg width="26" height="26" viewBox="0 0 24 24"><circle cx="12" cy="12" r="12" fill="var(--white)"/><rect x="6" y="8" width="12" height="8.5" rx="1" fill="var(--navy)"/><path d="M6.5 8.5 L12 13 L17.5 8.5" fill="none" stroke="var(--white)" stroke-width="1.3"/></svg>
      <span>LoremIpsumhasbeenindustry</span>
    </div>
    <div class="contact-row contact-detail">
      <svg width="26" height="26" viewBox="0 0 24 24"><g fill="none" stroke="var(--white)" stroke-width="1.6"><circle cx="12" cy="12" r="10"/><ellipse cx="12" cy="12" rx="4.5" ry="10"/><path d="M2 12 H22 M4 7 H20 M4 17 H20"/></g></svg>
      <span>LoremIpsumhasbeenindustry</span>
    </div>
  </div>

  <p class="about">We are a Retail Vacuum Repair shop and we also have Three carpet cleaning trucks that operate out of our location.</p>
</div>
</body>
</html>
```